Retail Cannabis Store Daily Promotions Graphic for Website/Social Media and Postcard

This project is for a business in Portland, Oregon called Marlow Leaf. We are a medical and recreational cannabis dispensary serving our neighborhoods since 2015. We would like to update some of our daily sales and need a new graphic to spread the word to the community. Ideally, we would like to use it on our social media, website and distribute it in our stores in the form of postcards.

It should be a simple run down of every day of the week and what promotions we have for that day. Additionally, we run a Veterans discount daily and would like to include a few calls to actions.

Target Market(s)

Cannabis users, adults between ages of 21 - 60.

Industry/Entity Type

Retail

Font styles to use
Other font styles liked:
• LetterGothicStd

Colors
aacf37
ffffff
9bcb3c
fcf9ce

Requirements
Must have
• I have attached our company logo files in ai format as well as our old daily deals graphic. For some additional color, we have been working towards revamping the feel of our brands and thus graphics. Attached you will see our latest designs (Attachments 4-6). We would like to follow a similar clean feel for the new daily deals graphic.
• Below is the language for the deals that need to be displayed on the graphic. The name of the deal (eg "Medible Monday") should be more prominent and the details that follow can be a bit more muted (possible suggestions: smaller font, under the deal name, etc) :
• Medible Monday - 15% Off All Edible Products
• $20 Tuesday - Select Flowers on Sale For $20/Eighth! (w/ tax)
• Topical Tuesday - 15% Off All Topical Products
• Waxy Wednesday - 15% Off All Concentrates, Extracts and Cartridges
• $30 Thursday - Select Top Shelf on Sale For $30/Eighth! (w/ tax)
• $1 Joint Friday - Get A 1/2g Joint for Just $1
• Shatterday - 15% Off All Concentrates, Extracts and Cartridges
• CBD Sunday - 15% Off All High CBD Products
• Veteran/Senior (65+) Receive 10% Discount Daily
• Ask About Our Neighborhood Discount Program
• Sign Up for Our Rewards Program And Start Saving
• Also, we need to include the following disclosure (can be in a smaller font, somewhere more discreet):
• "For use only by adults 21 years of age and older. Keep marijuana out of the reach of children. Do not operate a vehicle or machinery under the influence of this drug”

```html
<!DOCTYPE html>
<html lang="en">
<head>
<meta charset="utf-8">
<title>Marlow Leaf – Daily Deals</title>
<link rel="stylesheet" href="https://fonts.googleapis.com/css2?family=Alfa+Slab+One&family=Josefin+Sans:wght@700&family=Montserrat:wght@600;800&family=Roboto:ital,wght@0,400;1,400&display=swap">
<style>
  :root{
    --leaf-dark:#0c260d;
    --leaf-mid:#1f4f1c;
    --brand-green:#10b44c;
    --lime:#9bcb3c;
    --lime-fold:#557a12;
    --cyan:#14c6d0;
    --cyan-fold:#0a8d96;
    --cream:#fcf9ce;
    --white:#ffffff;
    --olive:#6e8f22;
    --tile-ink:#0f2a12;
  }
  *{margin:0;padding:0;box-sizing:border-box}
  html,body{width:857px;height:1200px;overflow:hidden;background:var(--leaf-dark)}
  .poster{position:relative;width:857px;height:1200px;overflow:hidden;
    font-family:"Roboto",sans-serif;color:var(--white)}
  .backdrop{position:absolute;inset:0;
    background:radial-gradient(ellipse at 45% 40%, #2f6a27 0%, var(--leaf-mid) 35%, var(--leaf-dark) 75%)}
  .shapes{position:absolute;inset:0}
  .brand{position:absolute;left:16px;top:34px;display:flex;align-items:center;gap:10px}
  .brand-dot{width:30px;height:30px;border-radius:50%;background:var(--cream)}
  .brand-name{font-family:"Josefin Sans",sans-serif;font-weight:700;font-size:30px;color:var(--cream);letter-spacing:1px}

  .tilt{position:absolute;transform:rotate(-8deg);transform-origin:left bottom;white-space:nowrap;line-height:1}
  .deal-name{font-family:"Josefin Sans",sans-serif;font-weight:700;font-size:30px;color:var(--cream);letter-spacing:1.5px;text-transform:uppercase}
  .deal-detail{font-family:"Roboto",sans-serif;font-style:italic;font-size:20px;color:var(--white);letter-spacing:.3px}
  .deal-detail.small{font-size:18.5px}

  .tiles{display:flex;gap:6px}
  .tile{width:56px;height:56px;background:var(--white);border:4px solid var(--tile-ink);outline:3px solid var(--white);
    display:flex;align-items:center;justify-content:center;
    font-family:"Alfa Slab One",serif;font-size:40px;color:var(--tile-ink)}

  .vertical{position:absolute;transform:rotate(-90deg);transform-origin:left top;white-space:nowrap;line-height:1}
  .senior-note{font-size:22px;color:var(--white);letter-spacing:.5px}
  .senior-offer{font-family:"Montserrat",sans-serif;font-weight:800;font-size:50px;color:var(--cyan);letter-spacing:1px}

  .neighbor{font-size:19px;color:var(--white)}
  .neighbor strong{font-family:"Montserrat",sans-serif;font-weight:800;font-size:32px;letter-spacing:1px}
  .signup{font-family:"Montserrat",sans-serif;font-weight:600;font-size:38px;color:var(--white)}
  .signup-sub{font-family:"Montserrat",sans-serif;font-weight:600;font-size:20px;color:var(--white);letter-spacing:.5px}
  .disclaimer{position:absolute;right:13px;top:1126px;text-align:right;font-size:14px;line-height:1.2;color:var(--olive)}
</style>
</head>
<body>
<main class="poster">
  <div class="backdrop" role="img" aria-label="Dark green photograph of cannabis leaves filling the background"></div>

  <svg class="shapes" viewBox="0 0 857 1200" aria-hidden="true">
    <polygon points="0,0 672,0 0,182" fill="var(--brand-green)"/>
    <!-- ribbon folds -->
    <polygon points="250,238 404,232 612,246 110,318" fill="var(--lime-fold)"/>
    <polygon points="330,420 452,420 684,444 150,492" fill="var(--lime-fold)"/>
    <polygon points="400,530 690,497 240,580" fill="var(--cyan-fold)"/>
    <polygon points="250,780 474,722 160,748" fill="var(--cyan-fold)"/>
    <polygon points="300,750 468,720 516,782" fill="var(--lime-fold)"/>
    <polygon points="360,850 690,800 520,906" fill="var(--lime-fold)"/>
    <!-- ribbons -->
    <polygon points="86,214 400,176 404,234 92,272" fill="var(--lime)"/>
    <polygon points="100,316 612,246 620,302 104,348" fill="var(--cyan)"/>
    <polygon points="112,424 448,372 452,424 118,468" fill="var(--lime)"/>
    <polygon points="124,518 684,442 690,498 128,552" fill="var(--cyan)"/>
    <polygon points="140,616 672,544 678,594 146,666" fill="var(--lime)"/>
    <polygon points="152,716 468,672 474,724 158,750" fill="var(--cyan)"/>
    <polygon points="164,816 686,750 690,800 170,868" fill="var(--lime)"/>
    <polygon points="178,920 516,872 522,920 184,968" fill="var(--cyan)"/>
    <!-- bottom bands -->
    <polygon points="0,1040 857,922 857,942 0,1060" fill="var(--lime-fold)"/>
    <polygon points="0,1060 857,942 857,1056 0,1176" fill="var(--cyan)"/>
    <polygon points="0,1176 857,1056 857,1074 0,1194" fill="var(--lime-fold)"/>
  </svg>

  <div class="brand">
    <span class="brand-dot"></span>
    <span class="brand-name">Marlow Leaf</span>
  </div>

  <div class="tilt tiles" style="left:452px;top:72px">
    <span class="tile">D</span><span class="tile">A</span><span class="tile">I</span><span class="tile">L</span><span class="tile">Y</span>
  </div>
  <div class="tilt tiles" style="left:478px;top:160px">
    <span class="tile">D</span><span class="tile">E</span><span class="tile">A</span><span class="tile">L</span><span class="tile">S</span>
  </div>

  <section class="deals">
    <div class="tilt deal-name" style="left:50px;top:180px">Medible Monday</div>
    <div class="tilt deal-detail" style="left:98px;top:226px">15% Off All Edible Products</div>

    <div class="tilt deal-name" style="left:76px;top:278px">$20 Tuesday</div>
    <div class="tilt deal-detail small" style="left:112px;top:332px">Select Flowers on Sale For $20/Eighth! (w/ tax)</div>

    <div class="tilt deal-name" style="left:78px;top:378px">Topical Tuesday</div>
    <div class="tilt deal-detail" style="left:126px;top:428px">15% Off All Topical Products</div>

    <div class="tilt deal-name" style="left:90px;top:482px">Waxy Wednesday</div>
    <div class="tilt deal-detail" style="left:138px;top:532px">15% Off All Concentrates, Extracts and Cartridges</div>

    <div class="tilt deal-name" style="left:104px;top:582px">$30 Thursday</div>
    <div class="tilt deal-detail small" style="left:152px;top:630px">Select Top Shelf on Sale For $30/Eighth! (w/ tax)</div>

    <div class="tilt deal-name" style="left:120px;top:682px">$1 Joint Friday</div>
    <div class="tilt deal-detail" style="left:164px;top:730px">Get A 1/2g Joint for Just $1</div>

    <div class="tilt deal-name" style="left:138px;top:778px">Shatterday</div>
    <div class="tilt deal-detail" style="left:178px;top:830px">15% Off All Concentrates, Extracts and Cartridges</div>

    <div class="tilt deal-name" style="left:154px;top:878px">CBD Sunday</div>
    <div class="tilt deal-detail" style="left:190px;top:934px">15% Off All High CBD Products</div>
  </section>

  <aside class="senior">
    <div class="vertical senior-note" style="left:746px;top:664px">Veteran/Senior (65+) Receive</div>
    <div class="vertical senior-offer" style="left:784px;top:802px">10% DISCOUNT DAILY</div>
  </aside>

  <div class="tilt neighbor" style="left:96px;top:998px">Ask About Our Neighborhood <strong>DISCOUNT PROGRAM</strong></div>
  <div class="tilt signup" style="left:340px;top:1034px">SIGN UP</div>
  <div class="tilt signup-sub" style="left:156px;top:1108px">FOR OUR REWARDS PROGRAM AND START SAVING</div>

  <p class="disclaimer">For use only by adults 21 years of age and older.<br>Keep marijuana out of the reach of children. Do not operate a<br>vehicle or machinery under the influence of this drug”</p>
</main>
</body>
</html>
```